Urgent * Legal Consultant Website Design

Provide a brief overview about your business Hello, website design required for independent legal consultant. Upload your company logo in the brief UPLOADED Specify the main navigation menu of your website (For better reference here's a sample of a website's navigation menu: (http://pixelrow.com/wp-content/uploads/2012/css-menu/ 3.jpg) Header menu should include: About Us, Our people, Services and Contact Us Indicate the subpages or the dropdown menu if you have any (Refer to: http://venmi.co/wp-content/uploads/2010 /11/nav.jpg) No Subpages in the dropdown Upload to separate file for the text or the content needed for the homepage (This is a helpful supporting file to provide in order for our designers to better understand the elements needed on how to layout your This could be in Word document if you're using Windows or in Pages if you are using Mac. ) GET your legal advice and protect you and your BUSINESS Family Law Debt Recovery Leases Crimes & Traffic, wills Violence Restraining Orders Probate Titles Shariah Law Provide some samples of Web designs you like for better reference (Cite 2 to 3 samples) Website must be clean , simple and display our services in a clear way. Examples: https://cdn.plinthora.com/wp/wp-content/uploads/sites/2/brisova-simple-business-wordpress-theme-1024x846.jpg https://cdn.plinthora.com/wp/wp -content / uploads / sites / 2 / corvelle-creative-studio-wp-website-template-1024x791.jpg Upload photos or files you would like to include in the design, or make mention if you are open to use stock photos Open to Use stock photos
Number of Pages Required
1 page

```html
<!DOCTYPE html>
<html lang="en">
<head>
<meta charset="utf-8">
<title>Corvane Legal Advisor</title>
<link href="https://fonts.googleapis.com/css2?family=Lato:wght@400;700;900&family=Open+Sans:ital,wght@0,400;0,600;0,700;1,400&display=swap" rel="stylesheet">
<style>
:root{
  --ink:#111111;
  --text:#555555;
  --muted:#888888;
  --red:#e0282e;
  --yellow:#f7e92b;
  --nav:#e8e8e8;
  --nav-dark:#6b6b6b;
  --panel:#f3f3f3;
  --footer:#f5f5f5;
  --line:#d8d8d8;
  --white:#ffffff;
}
*{margin:0;padding:0;box-sizing:border-box}
html,body{width:1200px;height:4500px;overflow:hidden;background:var(--white)}
body{position:relative;font-family:"Open Sans",Arial,sans-serif;color:var(--text)}
.abs{position:absolute}
h1,h2,h3,h4{font-family:"Lato",Arial,sans-serif;color:var(--ink)}
.btn{position:absolute;background:var(--yellow);color:var(--ink);border-radius:32px;font-family:"Lato",Arial,sans-serif;font-weight:900;font-size:16px;display:flex;align-items:center;justify-content:center;letter-spacing:.3px}

/* header */
.site-header{position:absolute;left:0;top:0;width:1200px;height:110px;background:var(--white)}
.brand{position:absolute;left:100px;top:24px;font-family:"Lato",Arial,sans-serif;font-weight:900;font-size:24px;color:var(--ink);letter-spacing:.5px}
.header-tools{position:absolute;left:1046px;top:34px;display:flex;gap:14px}
.main-nav{position:absolute;left:100px;top:86px;width:1000px;height:54px;background:var(--nav);font-family:"Lato",Arial,sans-serif;font-weight:700;font-size:14px;color:var(--ink)}
.main-nav span{position:absolute;top:0;height:54px;line-height:54px;white-space:nowrap}
.main-nav .active{background:var(--nav-dark);color:var(--white);padding:0 14px}
.dropdown{position:absolute;left:717px;top:140px;width:220px;height:244px;background:var(--nav-dark);padding:12px 16px;font-size:13px;color:var(--white);line-height:27px;white-space:nowrap}

/* hero */
.hero{position:absolute;left:0;top:110px;width:1200px;height:552px;background:linear-gradient(90deg,#fbfbfb 0%,#f2f2f2 45%,#cfcfcf 75%,#e9e9e9 100%)}
.hero-title{position:absolute;left:100px;top:256px;font-size:48px;font-weight:900;line-height:63px;letter-spacing:-.3px;white-space:nowrap}

/* services */
.section-title{position:absolute;left:0;width:1200px;text-align:center;font-family:"Lato",Arial,sans-serif;font-weight:900;font-size:44px;color:var(--ink)}
.service{position:absolute;width:230px}
.service svg{display:block;width:54px;height:54px}
.service h3{font-size:17px;font-weight:700;margin-top:26px;white-space:nowrap}
.service p{font-size:14px;line-height:25px;margin-top:14px}

/* about */
.about{position:absolute;left:0;top:1385px;width:1200px;height:552px;background:linear-gradient(90deg,#f4f4f4 0%,#ececec 45%,#d7d7d7 65%,#bdbdbd 85%,#8e9096 100%)}
.about h2{position:absolute;left:100px;top:80px;font-size:42px;line-height:56px;font-weight:900;white-space:nowrap}
.about p{position:absolute;left:100px;top:215px;width:560px;font-size:14px;line-height:26px;color:#444}

/* news */
.news-card{position:absolute;top:2130px;width:308px;height:410px}
.news-photo{position:absolute;left:0;top:0;width:308px;height:230px}
.news-body{position:absolute;left:16px;top:194px;width:276px;height:216px;background:var(--white);box-shadow:0 2px 10px rgba(0,0,0,.08);padding:26px 20px}
.news-body h3{font-size:19px;font-weight:700;white-space:nowrap}
.news-body p{font-size:14px;line-height:22px;margin-top:10px}
.news-meta{border-top:1px solid var(--line);margin-top:16px;padding-top:14px;font-size:13px;display:flex;align-items:center;gap:6px}

/* testimonial */
.testimonial{position:absolute;left:0;top:2633px;width:1200px;height:528px;background:linear-gradient(90deg,#c9c4bd 0%,#e0dbd3 25%,#ededed 40%,#f4f4f4 100%)}
.testimonial blockquote{position:absolute;left:555px;top:215px;width:555px;font-style:italic;font-size:15px;line-height:28px;color:#333}
.testimonial cite{position:absolute;left:555px;top:385px;font-style:normal;font-family:"Lato",Arial,sans-serif;font-weight:700;font-size:20px;color:var(--ink)}

/* people */
.person-card{position:absolute;width:334px;height:278px;background:var(--panel);text-align:center;padding-top:40px}
.person-card h3{font-size:30px;font-weight:400}
.person-card .role{color:var(--red);font-size:15px;margin-top:4px}
.person-card p{font-size:13px;line-height:22px;margin:16px auto 0;width:230px}
.person-card .links{display:flex;justify-content:center;gap:10px;margin-top:14px}
.person-photo{position:absolute;width:334px;height:278px;background:linear-gradient(180deg,#ffffff 0%,#f0f0f0 55%,#2b2d33 56%,#1e2026 100%)}

/* footer */
.site-footer{position:absolute;left:0;top:4015px;width:1200px;height:485px;background:var(--footer)}
.site-footer h4{position:absolute;font-size:20px;font-weight:700}
.field{position:absolute;background:var(--white);border:1px solid #bdbdbd;font-size:12px;color:#777;padding:6px 10px}
.contact-item{position:absolute;left:777px;display:flex;gap:20px;align-items:flex-start;font-size:12px;line-height:20px;color:#555}
.contact-item .dot{flex:none;width:32px;height:32px;border-radius:50%;background:#fbe0e0;display:flex;align-items:center;justify-content:center}
.social{position:absolute;left:777px;top:4325px;display:flex;gap:10px}
.social span{width:34px;height:34px;border-radius:50%;display:block}
.copyright{position:absolute;left:0;top:4440px;width:1200px;text-align:center;font-size:12px;color:#777}
</style>
</head>
<body>

<header class="site-header">
  <div class="brand">CORVANE LEGAL</div>
  <div class="header-tools">
    <svg width="16" height="16" viewBox="0 0 16 16"><circle cx="6.5" cy="6.5" r="5" fill="none" stroke="#333" stroke-width="2"/><line x1="10" y1="10" x2="15" y2="15" stroke="#333" stroke-width="2"/></svg>
    <svg width="16" height="16" viewBox="0 0 16 16"><circle cx="8" cy="5" r="3.5" fill="#333"/><path d="M1 16c0-5 3-7 7-7s7 2 7 7z" fill="#333"/></svg>
  </div>
</header>

<section class="hero" role="img" aria-label="Photo of hands typing on a laptop at a bright office desk"></section>
<h1 class="hero-title">GET YOUR LEGAL ADVICE<br>AND PROTECT YOU AND<br>YOUR BUSINESS</h1>
<div class="btn" style="left:100px;top:485px;width:182px;height:62px">GET MORE INFO</div>

<nav class="main-nav">
  <span style="left:95px">HOME</span>
  <span style="left:248px">ABOUT US</span>
  <span style="left:432px">OUR PEOPLE</span>
  <span class="active" style="left:617px">SERVICES</span>
  <span style="left:810px">CONTACT US</span>
</nav>
<div class="dropdown">
  Family Law<br>Debt Recovery<br>Leases<br>Crimes &amp; Traffic, wills<br>Violence Restraining Orders<br>Probate<br>Titles<br>Shariah Law
</div>

<h2 class="section-title" style="top:745px">SERVICES</h2>

<div class="service" style="left:100px;top:852px">
  <svg viewBox="0 0 54 54" fill="none" stroke="#e0282e" stroke-width="2"><circle cx="17" cy="14" r="6"/><circle cx="37" cy="14" r="6"/><circle cx="27" cy="28" r="5"/><path d="M6 40c0-8 5-13 11-13M48 40c0-8-5-13-11-13M18 48c0-7 4-11 9-11s9 4 9 11z"/></svg>
  <h3>Family Law</h3>
  <p>Nam libero tempore, cum soluto bis est eligendi optio cumquenm pedit quo minus id qu.</p>
</div>
<div class="service" style="left:363px;top:852px">
  <svg viewBox="0 0 54 54" fill="none" stroke="#e0282e" stroke-width="2"><rect x="4" y="15" width="46" height="26" rx="2"/><rect x="9" y="20" width="36" height="16"/><circle cx="27" cy="28" r="6"/></svg>
  <h3>Debt Recovery</h3>
  <p>Nam libero tempore, cum soluto bis est eligendi optio cumquenm pedit quo minus id qu.</p>
</div>
<div class="service" style="left:628px;top:852px">
  <svg viewBox="0 0 54 54" fill="none" stroke="#e0282e" stroke-width="2"><path d="M5 27L27 8l22 19"/><path d="M11 22v24h32V22"/><rect x="22" y="32" width="10" height="14"/></svg>
  <h3>Leases</h3>
  <p>Nam libero tempore, cum soluto bis est eligendi optio cumquenm pedit quo minus id qu.</p>
</div>
<div class="service" style="left:892px;top:852px">
  <svg viewBox="0 0 54 54" fill="none" stroke="#e0282e" stroke-width="2"><line x1="27" y1="6" x2="27" y2="46"/><line x1="9" y1="12" x2="45" y2="12"/><path d="M9 12L3 28h12zM45 12l-6 16h12zM3 28a6 5 0 0 0 12 0M39 28a6 5 0 0 0 12 0"/><line x1="17" y1="47" x2="37" y2="47"/></svg>
  <h3>Crimes &amp; Traffic, wills</h3>
  <p>Nam libero tempore, cum soluto bis est eligendi optio cumquenm pedit quo minus id qu.</p>
</div>

<div class="service" style="left:100px;top:1092px">
  <svg viewBox="0 0 54 54" fill="none" stroke="#e0282e" stroke-width="2"><path d="M10 4h24l10 10v36H10z"/><path d="M34 4v10h10"/><line x1="17" y1="24" x2="37" y2="24"/><line x1="17" y1="31" x2="37" y2="31"/><line x1="17" y1="38" x2="30" y2="38"/></svg>
  <h3>Probate</h3>
  <p>Nam libero tempore, cum soluto bis est eligendi optio cumquenm pedit quo minus id qu.</p>
</div>
<div class="service" style="left:363px;top:1092px">
  <svg viewBox="0 0 54 54" fill="none" stroke="#e0282e" stroke-width="2"><path d="M6 6h20l22 22-20 20L6 26z"/><circle cx="16" cy="16" r="4"/></svg>
  <h3>Titles</h3>
  <p>Nam libero tempore, cum soluto bis est eligendi optio cumquenm pedit quo minus id qu.</p>
</div>
<div class="service" style="left:628px;top:1092px">
  <svg viewBox="0 0 54 54" fill="none" stroke="#e0282e" stroke-width="2"><path d="M5 18L27 6l22 12z"/><line x1="5" y1="22" x2="49" y2="22"/><line x1="11" y1="26" x2="11" y2="42"/><line x1="21" y1="26" x2="21" y2="42"/><line x1="33" y1="26" x2="33" y2="42"/><line x1="43" y1="26" x2="43" y2="42"/><rect x="4" y="44" width="46" height="5"/></svg>
  <h3>Shariah Law</h3>
  <p>Nam libero tempore, cum soluto bis est eligendi optio cumquenm pedit quo minus id qu.</p>
</div>
<div class="service" style="left:892px;top:1092px">
  <svg viewBox="0 0 54 54" fill="none" stroke="#e0282e" stroke-width="2"><rect x="20" y="4" width="14" height="24" rx="2" transform="rotate(-45 27 16)"/><line x1="24" y1="26" x2="46" y2="48"/><rect x="4" y="44" width="22" height="5"/></svg>
  <h3>Violence Restraining Orders</h3>
  <p>Nam libero tempore, cum soluto bis est eligendi optio cumquenm pedit quo minus id qu.</p>
</div>

<section class="about" role="img" aria-label="Photo of a hand signing a contract with a pen">
  <h2>ABOUT<br>CORVANE LEGAL ADVISOR</h2>
  <p>Nemo enim ipsam voluptatem quia voluptas sit aspernatur aut odit aut fugit, sed quia consequuntur magni dolores eos qui ratione voluptatem sequi nesciunt. Neque porro quisquam est, qui dolorem ipsum quia dolor sit amet, consectetur, adipisci velit, sed quia non numquam eius modi tempora incidunt ut labore et dolore magnam aliquam quaerat voluptatem. Ut enim ad minima veniam, quis nostrum exercitationem ullam corporis suscipit laboriosam, nisi ut aliquid ex.</p>
</section>
<div class="btn" style="left:100px;top:1805px;width:158px;height:62px">READ MORE</div>

<h2 class="section-title" style="top:2030px">LATEST NEWS</h2>

<article class="news-card" style="left:100px">
  <div class="news-photo" role="img" aria-label="Photo of people shaking hands over a desk" style="background:linear-gradient(135deg,#6d5a4c,#c9b9a7 55%,#8a7563)"></div>
  <div class="news-body"><h3>Finibus Bonorut Malorum</h3><p>Nemo enim ipsam voluptatem quia voluptas sit aspernatur aut odit aut fugit, sed quia consequ.</p>
    <div class="news-meta"><svg width="12" height="12" viewBox="0 0 12 12"><rect x="1" y="2" width="10" height="9" fill="#e0282e"/></svg>04/09/2018 &nbsp;| <svg width="12" height="12" viewBox="0 0 12 12"><circle cx="6" cy="4" r="3" fill="#e0282e"/><path d="M1 12c0-4 2-5 5-5s5 1 5 5z" fill="#e0282e"/></svg>Tobin Ashe</div></div>
</article>
<article class="news-card" style="left:447px">
  <div class="news-photo" role="img" aria-label="Photo of a hand writing on documents" style="background:linear-gradient(135deg,#b7a08d,#e6dcd2 55%,#a88f7c)"></div>
  <div class="news-body"><h3>Finibus Bonorut Malorum</h3><p>Nemo enim ipsam voluptatem quia voluptas sit aspernatur aut odit aut fugit, sed quia consequ.</p>
    <div class="news-meta"><svg width="12" height="12" viewBox="0 0 12 12"><rect x="1" y="2" width="10" height="9" fill="#e0282e"/></svg>04/09/2018 &nbsp;| <svg width="12" height="12" viewBox="0 0 12 12"><circle cx="6" cy="4" r="3" fill="#e0282e"/><path d="M1 12c0-4 2-5 5-5s5 1 5 5z" fill="#e0282e"/></svg>Tobin Ashe</div></div>
</article>
<article class="news-card" style="left:793px">
  <div class="news-photo" role="img" aria-label="Photo of a street demonstration with protest signs" style="background:linear-gradient(135deg,#4f4a48,#8d8580 50%,#3a3634)"></div>
  <div class="news-body"><h3>Finibus Bonorut Malorum</h3><p>Nemo enim ipsam voluptatem quia voluptas sit aspernatur aut odit aut fugit, sed quia consequ.</p>
    <div class="news-meta"><svg width="12" height="12" viewBox="0 0 12 12"><rect x="1" y="2" width="10" height="9" fill="#e0282e"/></svg>04/09/2018 &nbsp;| <svg width="12" height="12" viewBox="0 0 12 12"><circle cx="6" cy="4" r="3" fill="#e0282e"/><path d="M1 12c0-4 2-5 5-5s5 1 5 5z" fill="#e0282e"/></svg>Tobin Ashe</div></div>
</article>

<section class="testimonial" role="img" aria-label="Photo of a smiling client seated at a desk">
  <svg class="abs" style="left:555px;top:95px" width="92" height="78" viewBox="0 0 92 78"><path d="M0 40C0 15 12 3 36 0v14C22 17 17 25 17 36h19v42H0zM56 40C56 15 68 3 92 0v14C78 17 73 25 73 36h19v42H56z" fill="#e0282e"/></svg>
  <blockquote>Nemo enim ipsam voluptatem quia voluptas sit aspernatur aut odit aut fugit, sed quia consequuntur magni dolores eos qui ratione voluptatem sequi nesciunque porro quisquam est, qui dolorem ipsum quia dolor sit amet, consectetur, adipisci velit, sed quia non numquam eius modi tempora incidunt ut labore et dolore mag nam aliquam quaerat voluptatem.</blockquote>
  <cite>- Walter Brisk</cite>
  <svg class="abs" style="left:1055px;top:405px" width="46" height="20" viewBox="0 0 46 20"><circle cx="10" cy="10" r="9" fill="#666"/><path d="M12 5l-5 5 5 5" stroke="#fff" stroke-width="2" fill="none"/><circle cx="36" cy="10" r="9" fill="#666"/><path d="M34 5l5 5-5 5" stroke="#fff" stroke-width="2" fill="none"/></svg>
</section>

<h2 class="section-title" style="top:3240px">MEET OUR PEOPLE</h2>

<div class="person-card" style="left:100px;top:3355px"><h3>Dorian Vale</h3><div class="role">Vice President</div><p>Ut enim ad minima veniam, quis nos trum exercitationem ullam corporis su scipit laboriosam, nisi ut ali</p><div class="links"><span style="width:8px;height:8px;background:#777;display:block"></span><span style="width:8px;height:8px;background:#777;display:block"></span><span style="width:8px;height:8px;background:#777;display:block"></span></div></div>
<div class="person-photo" role="img" aria-label="Portrait of a female lawyer in a dark suit" style="left:433px;top:3355px"></div>
<div class="person-card" style="left:767px;top:3355px"><h3>Marcus Fennel</h3><div class="role">Vice President</div><p>Ut enim ad minima veniam, quis nos trum exercitationem ullam corporis su scipit laboriosam, nisi ut ali</p><div class="links"><span style="width:8px;height:8px;background:#777;display:block"></span><span style="width:8px;height:8px;background:#777;display:block"></span><span style="width:8px;height:8px;background:#777;display:block"></span></div></div>

<div class="person-photo" role="img" aria-label="Portrait of a senior male lawyer in a dark suit" style="left:100px;top:3633px"></div>
<div class="person-card" style="left:433px;top:3633px"><h3>Lisette</h3><div class="role">Vice President</div><p>Ut enim ad minima veniam, quis nos trum exercitationem ullam corporis su scipit laboriosam, nisi ut ali</p><div class="links"><span style="width:8px;height:8px;background:#777;display:block"></span><span style="width:8px;height:8px;background:#777;display:block"></span><span style="width:8px;height:8px;background:#777;display:block"></span></div></div>
<div class="person-photo" role="img" aria-label="Portrait of a male lawyer in a dark suit" style="left:767px;top:3633px"></div>

<footer class="site-footer">
  <h4 style="left:95px;top:58px">Contact form</h4>
  <div class="field" style="left:95px;top:120px;width:310px;height:34px">Name</div>
  <div class="field" style="left:415px;top:120px;width:310px;height:34px">Phone no</div>
  <div class="field" style="left:95px;top:172px;width:630px;height:34px">Email</div>
  <div class="field" style="left:95px;top:212px;width:630px;height:80px">Message</div>
  <div class="btn" style="left:628px;top:308px;width:94px;height:32px;font-size:13px">SUBMIT</div>

  <h4 style="left:777px;top:58px">Contact Information</h4>
  <h4 style="left:777px;top:265px">Social Media</h4>
  <div style="position:absolute;left:95px;top:390px;width:1005px;height:1px;background:var(--line)"></div>
  <svg class="abs" style="left:1070px;top:417px" width="26" height="16" viewBox="0 0 26 16"><path d="M2 14L13 3l11 11" stroke="#999" stroke-width="2.5" fill="none"/></svg>
</footer>

<div class="contact-item" style="top:4115px"><span class="dot"><svg width="12" height="16" viewBox="0 0 12 16"><path d="M6 0a6 6 0 0 1 6 6c0 4-6 10-6 10S0 10 0 6a6 6 0 0 1 6-6z" fill="#e0282e"/><circle cx="6" cy="6" r="2" fill="#fbe0e0"/></svg></span><span>418 Harrow Line, Unit 9 Elmbridge, Caldor<br>Regional Municipality, Westmark K2P 4R8</span></div>
<div class="contact-item" style="top:4180px"><span class="dot"><svg width="14" height="14" viewBox="0 0 14 14"><path d="M3 0l3 3-2 2a8 8 0 0 0 5 5l2-2 3 3-2 3C6 14 0 8 0 3z" fill="#e0282e"/></svg></span><span style="line-height:32px">1 555 014 2277</span></div>
<div class="contact-item" style="top:4230px"><span class="dot"><svg width="14" height="10" viewBox="0 0 14 10"><rect width="14" height="10" fill="#e0282e"/><path d="M0 0l7 6 7-6" stroke="#fbe0e0" fill="none"/></svg></span><span style="line-height:32px">info@corvanelegaladvisor.com</span></div>
<div class="social"><span style="background:#3b5998"></span><span style="background:#1da1f2"></span><span style="background:#0e76a8"></span><span style="background:#e0282e"></span></div>
<div class="copyright">Copyright © 2018, Corvane Legal Advisor . All rights reserved.</div>

</body>
</html>
```